Every Drawer Neatly Sorted or EDN Organized needs a business card design. EDN Organized is a professi

We need a business card design that is clean, sharp and conveys a sense of organization. I already have a logo.

Target Market(s)

Families (specifically mothers), small business owners, parents, seniors

Industry/Entity Type

Business

Contact Information for Business Card

My website is www.ednorganized-example.com and my Facebook page is http://www.socialpage-example.com/everydrawerneatlysorted. The phone number is 555-418-2706 and I want to be listed as Miriel O. Dunsford, Owner

Requirements
Must have
• My logo.

```html
<!DOCTYPE html>
<html lang="en">
<head>
<meta charset="utf-8">
<title>EDN Organized — Business Card</title>
<link rel="stylesheet" href="https://fonts.googleapis.com/css2?family=Open+Sans:wght@300;400&display=swap">
<style>
  :root {
    --stage: #3a3a3c;
    --card: #1c1c1e;
    --card-edge: #0e0e0f;
    --brand-blue: #1a84e0;
    --ink-white: #e9e9ea;
    --ink-grey: #b9b9bc;
  }
  * { margin: 0; padding: 0; box-sizing: border-box; }
  html, body { width: 1200px; height: 840px; overflow: hidden; }
  body {
    background: var(--stage);
    font-family: "Open Sans", Arial, sans-serif;
    display: flex;
    align-items: center;
    justify-content: center;
    gap: 60px;
  }
  .card {
    position: relative;
    width: 520px;
    height: 297px;
    background: var(--card);
    border-radius: 3px;
    box-shadow: 0 3px 0 var(--card-edge), 0 14px 30px rgba(0,0,0,0.45);
    overflow: hidden;
  }

  /* Business name: one colour, one weight */
  .business-name {
    display: flex;
    align-items: center;
    gap: 10px;
    white-space: nowrap;
    color: var(--ink-white);
    font-weight: 300;
  }
  .name-marker {
    width: 12px;
    height: 12px;
    background: var(--brand-blue);
    flex: none;
  }

  .card-front .business-name {
    position: absolute;
    left: 50%;
    top: 50%;
    transform: translate(-50%, -50%);
    font-size: 22px;
  }

  .card-back .business-name {
    position: absolute;
    right: 34px;
    top: 42px;
    font-size: 16px;
  }

  .contact {
    position: absolute;
    left: 290px;
    top: 112px;
  }
  .contact .person {
    color: var(--brand-blue);
    font-size: 15px;
    font-weight: 400;
    line-height: 1.2;
  }
  .contact .role {
    color: var(--ink-grey);
    font-size: 11px;
    font-weight: 300;
    margin: 2px 0 10px 0;
  }
  .contact ul { list-style: none; }
  .contact li {
    display: flex;
    align-items: center;
    gap: 6px;
    color: var(--ink-grey);
    font-size: 10.5px;
    font-weight: 300;
    line-height: 17px;
  }
  .contact svg { width: 10px; height: 10px; flex: none; }

  .short-name {
    position: absolute;
    left: 40px;
    bottom: 36px;
    color: var(--brand-blue);
    font-weight: 300;
    font-size: 32px;
    line-height: 1;
    white-space: nowrap;
  }
</style>
</head>
<body>
  <section class="card card-front" aria-label="Card front">
    <div class="business-name">
      <span class="name-marker" aria-hidden="true"></span>
      <span>Every Drawer Neatly Sorted</span>
    </div>
  </section>

  <section class="card card-back" aria-label="Card back">
    <div class="business-name">
      <span>Every Drawer Neatly Sorted</span>
    </div>

    <div class="contact">
      <p class="person">Miriel O. Dunsford</p>
      <p class="role">Owner</p>
      <ul>
        <li>
          <svg viewBox="0 0 10 10" aria-hidden="true"><path d="M2 0.5 L3.6 0.5 L4.2 3 L3 3.8 Q4 6 6.2 7 L7 5.8 L9.5 6.4 L9.5 8 Q9.5 9.5 8 9.5 Q0.5 9 0.5 2 Q0.5 0.5 2 0.5 Z" fill="#1a84e0"/></svg>
          555-418-2706
        </li>
        <li>
          <svg viewBox="0 0 10 10" aria-hidden="true"><circle cx="5" cy="5" r="4.3" fill="none" stroke="#1a84e0" stroke-width="1.2"/><ellipse cx="5" cy="5" rx="1.8" ry="4.3" fill="none" stroke="#1a84e0" stroke-width="0.9"/><line x1="0.7" y1="5" x2="9.3" y2="5" stroke="#1a84e0" stroke-width="0.9"/></svg>
          www.ednorganized-example.com
        </li>
        <li>
          <svg viewBox="0 0 10 10" aria-hidden="true"><rect x="0.5" y="0.5" width="9" height="9" rx="1.5" fill="#1a84e0"/></svg>
          everydrawerneatlysorted
        </li>
      </ul>
    </div>

    <span class="short-name">EDN Organized</span>
  </section>
</body>
</html>
```